Student Business Card Design

As you already know, I'm a student at BV majoring in Supply Chain & Logistics Technology. I want a business card design that leaves the recipient impressed. A clean, professional, and memorable design is desired without too much color. My school's logo can be found online. I'd like to have that on the card.

Target Market(s)

Anyone who is a recruiter or an employer who has authority to hire.

Industry/Entity Type

Business

Contact Information for Business Card

Name: Osman Velibor

Phone Number: 614-275-3316

Email Address: velibor.osman@mailbox-demo.net

Major: Supply Chain & Logistics Technology

Minor: Purchasing

University: Marlowe State University

College: Ashcombe School of Engineering

I want a Workvine logo with my name beside it.

Also, on the back of the card I want this quote: "If it doesn't challenge you, it doesn't change you"-, Lena Sorbach

Requirements
Must have
• I'd like to see a Workvine logo go with my name.
• Professional-I'm going to be handing this card out in career fairs and networking events.
Nice to have
• Marlowe State University's colors: white, silver, and red, but if you feel it's better to go with a different color scheme then do it.
Should not have
• No white space on the design.

```html
<!DOCTYPE html>
<html lang="en">
<head>
<meta charset="utf-8">
<title>Osman Velibor – Business Card</title>
<link rel="stylesheet" href="https://fonts.googleapis.com/css2?family=Gelasio:wght@400&family=Arimo:wght@400&family=Noto+Sans:wght@400;500&display=swap">
<style>
  :root {
    --stage: #1c1c1c;
    --card-light: #efefef;
    --card-dark: #030303;
    --accent-blue: #3d37cf;
    --ink-dark: #0b0b0b;
    --ink-light: #f2f2f2;
  }
  * { margin: 0; padding: 0; box-sizing: border-box; }
  html, body { width: 1200px; height: 800px; overflow: hidden; }
  body { background: var(--stage); position: relative; }

  .card {
    position: absolute;
    top: 238px;
    width: 536px;
    height: 306px;
    overflow: hidden;
  }
  .card--front { left: 49px; background: var(--card-light); }
  .card--back { left: 617px; background: var(--card-dark); }

  .card__waves { position: absolute; inset: 0; width: 100%; height: 100%; }

  .front__name {
    position: absolute;
    left: 28px;
    top: 36px;
    font-family: "Gelasio", Georgia, serif;
    font-size: 48px;
    font-weight: 400;
    line-height: 1;
    color: var(--ink-dark);
  }
  .front__fields {
    position: absolute;
    left: 36px;
    top: 91px;
    font-family: "Arimo", Arial, sans-serif;
    font-size: 15px;
    line-height: 18px;
    color: var(--ink-dark);
  }

  .front__school {
    position: absolute;
    right: 31px;
    top: 152px;
    text-align: right;
    font-family: "Noto Sans", sans-serif;
    font-size: 14px;
    line-height: 21px;
    letter-spacing: 0.2px;
    color: var(--ink-light);
  }

  .front__contacts {
    position: absolute;
    right: 31px;
    top: 214px;
    list-style: none;
    font-family: "Arimo", Arial, sans-serif;
    font-size: 14px;
    line-height: 20.5px;
    color: var(--ink-light);
  }
  .contact {
    display: flex;
    justify-content: flex-end;
    align-items: center;
    gap: 13px;
  }
  .contact__icon { width: 10px; height: 10px; flex: none; }
  .contact__mark { width: 9px; height: 9px; background: var(--ink-light); flex: none; margin-right: 0.5px; }

  .back__content {
    position: absolute;
    inset: 0;
    text-align: center;
    color: var(--ink-light);
  }
  .back__name {
    position: absolute;
    left: 0; right: 0;
    top: 104px;
    font-family: "Gelasio", Georgia, serif;
    font-size: 48px;
    line-height: 1;
    font-weight: 400;
  }
  .back__quote {
    position: absolute;
    left: 0; right: 0;
    top: 158px;
    font-family: "Noto Sans", sans-serif;
    font-size: 17px;
    letter-spacing: 0.4px;
  }
  .back__author {
    position: absolute;
    left: 0; right: 0;
    top: 187px;
    font-family: "Noto Sans", sans-serif;
    font-weight: 500;
    font-size: 17px;
    letter-spacing: 0.3px;
  }
</style>
</head>
<body>

<section class="card card--front" aria-label="Front of business card">
  <svg class="card__waves" viewBox="0 0 670 382" preserveAspectRatio="none" aria-hidden="true">
    <path fill="var(--card-dark)" d="M670,105 C560,82 440,110 370,200 C300,290 220,352 130,350 C70,348 25,322 0,282 L0,382 L670,382 Z"/>
    <path fill="var(--accent-blue)" d="M450,128 C520,88 600,70 670,80 L670,106 C590,88 520,100 450,128 Z"/>
    <path fill="var(--accent-blue)" d="M0,276 C25,318 70,338 120,340 C165,342 210,318 245,283 C205,312 165,328 125,328 C75,328 30,310 0,290 Z"/>
  </svg>

  <h1 class="front__name">Osman Velibor</h1>
  <p class="front__fields">Supply Chain &amp; Logistics Technology<br>Purchasing</p>

  <p class="front__school">Marlowe State University<br>Ashcombe School of Engineering</p>

  <ul class="front__contacts">
    <li class="contact"><span>Workvine · OsmanVelibor</span><span class="contact__mark" aria-hidden="true"></span></li>
    <li class="contact"><span>614-275-3316</span>
      <svg class="contact__icon" viewBox="0 0 10 10" aria-hidden="true">
        <rect width="10" height="10" fill="var(--ink-light)"/>
        <path d="M2,3 Q5,1 8,3 L7,4 L6,3.5 L4,3.5 L3,4 Z M3,5 L7,5 L8,8 L2,8 Z" fill="var(--card-dark)"/>
      </svg>
    </li>
    <li class="contact"><span>velibor.osman@mailbox-demo.net</span>
      <svg class="contact__icon" viewBox="0 0 10 10" aria-hidden="true">
        <rect width="10" height="10" fill="var(--ink-light)"/>
        <rect x="1.8" y="3" width="6.4" height="4.4" fill="var(--card-dark)"/>
        <path d="M1.8,3 L5,5.6 L8.2,3" stroke="var(--ink-light)" stroke-width="0.7" fill="none"/>
      </svg>
    </li>
  </ul>
</section>

<section class="card card--back" aria-label="Back of business card">
  <div class="back__content">
    <h2 class="back__name">Osman Velibor</h2>
    <p class="back__quote">"If it doesn't challenge you, it doesn't change you"</p>
    <p class="back__author">Lena Sorbach</p>
  </div>
</section>

</body>
</html>
```